Peanut Butter - Single Serve Sachet

We are a sports and wellness nutrition company (https://www.brimleyfuel.in) and launching a new product Peanut Butter. Need attractive design of single serve sachet.

The product should be unique and eye catchy. It should have enough space to mention USPs later.

The product USP is tear-on the go sachet, image mockup has been attached.

Target Market(s)

Sports Persons and General Public looking for Peanut Butter.

Industry/Entity Type

Nutrition

Colors

Designer to choose colors to be used in the design.

Requirements
Must have
• Single serve sachet design. Attractive colour theme with Peanut Butter mentioned as bold.
Should not have
• no black colour

```html
<!DOCTYPE html>
<html lang="en">
<head>
<meta charset="utf-8">
<title>Peanut Butter – Single Serve Sachet</title>
<link href="https://fonts.googleapis.com/css2?family=Caveat+Brush&family=Amatic+SC:wght@400;700&family=Montserrat:wght@400;500;600&display=swap" rel="stylesheet">
<style>
  :root {
    --backdrop: #dcdcdc;
    --pouch: #f6f6f4;
    --gold: #d3b236;
    --gold-soft: #e2c75a;
    --ink: #4a4a4a;
    --ink-soft: #5a5a5a;
    --pattern-a: #ece6d6;
    --pattern-b: #d9c79a;
  }
  * { margin: 0; padding: 0; box-sizing: border-box; }
  html, body { width: 1200px; height: 800px; overflow: hidden; }
  body {
    background: var(--backdrop);
    font-family: "Montserrat", sans-serif;
    position: relative;
  }
  .pouch {
    position: absolute;
    top: 81px;
    width: 411px;
    height: 648px;
    background: var(--pouch);
    border-radius: 14px 14px 6px 6px;
    overflow: hidden;
  }
  .pouch--front { left: 147px; }
  .pouch--back { left: 723px; }

  .pattern {
    position: absolute;
    left: 0; right: 0;
    background: linear-gradient(135deg, var(--pattern-a), var(--pattern-b) 50%, var(--pattern-a));
  }
  .pattern--top { top: 0; height: 80px; }
  .pattern--side-left { top: 80px; left: 0; right: auto; width: 34px; height: 240px; }
  .pattern--side-right { top: 80px; right: 0; left: auto; width: 34px; height: 240px; }
  .pattern--bottom { bottom: 0; height: 88px; }

  .speech-bubble { position: absolute; left: 36px; top: 74px; width: 340px; height: 330px; }

  .product-title {
    position: absolute;
    left: 36px; width: 340px;
    top: 80px;
    text-align: center;
    font-family: "Caveat Brush", cursive;
    color: var(--ink);
    font-size: 104px;
    line-height: 94px;
  }
  .product-format {
    position: absolute;
    left: 36px; width: 340px;
    top: 292px;
    text-align: center;
    font-family: "Amatic SC", cursive;
    color: #fff;
    font-size: 46px;
    letter-spacing: 1px;
  }
  .flavour-name {
    position: absolute;
    left: 0; right: 0;
    top: 392px;
    text-align: center;
    font-family: "Amatic SC", cursive;
    color: var(--gold);
    font-size: 60px;
    font-weight: 400;
    line-height: 1;
  }
  .variant {
    position: absolute;
    left: 0; right: 0;
    top: 456px;
    text-align: center;
    color: var(--gold);
    font-weight: 600;
    font-size: 22px;
    letter-spacing: 1px;
  }
  .knife {
    position: absolute;
    border-radius: 20px;
  }
  .pouch--front .knife {
    left: 55px; width: 300px; top: 488px; height: 36px;
    background: linear-gradient(90deg, #e9e9e6, #cfcfcc);
  }
  .pouch--back .knife {
    left: 70px; width: 270px; top: 212px; height: 30px;
    background: linear-gradient(90deg, #f1e6bb, #e2c75a);
  }
  .organic-band {
    position: absolute;
    left: 0; right: 0; bottom: 0;
    height: 110px;
    background: var(--gold);
  }
  .organic-label {
    position: absolute;
    left: 0; right: 0;
    top: 540px;
    text-align: center;
    color: #fff6d4;
    font-weight: 600;
    font-size: 22px;
    letter-spacing: 1px;
  }
  .origin {
    position: absolute;
    left: 0; right: 0;
    top: 590px;
    text-align: center;
    color: var(--ink);
    font-weight: 600;
    font-size: 20px;
  }

  .info-frame {
    position: absolute;
    left: 12px; right: 12px;
    top: 80px; bottom: 88px;
    border: 2px solid var(--gold);
    background: var(--pouch);
  }
  .claim {
    position: absolute;
    left: 0; right: 0;
    top: 108px;
    text-align: center;
    color: var(--gold-soft);
    font-weight: 600;
    font-size: 21px;
    line-height: 27px;
  }
  .free-from {
    position: absolute;
    left: 0; right: 0;
    top: 262px;
    text-align: center;
    color: var(--ink);
    font-weight: 600;
    font-size: 17px;
  }
  .no-oils {
    position: absolute;
    left: 0; right: 0;
    top: 292px;
    text-align: center;
    color: var(--gold);
    font-weight: 600;
    font-size: 21px;
  }
  .ingredients-line {
    position: absolute;
    left: 36px; right: 36px;
    top: 330px;
    color: var(--ink-soft);
    font-size: 15px;
    line-height: 19px;
  }
  .ingredients-line strong { color: var(--gold); font-weight: 600; }
  .ingredients-heading {
    position: absolute;
    left: 0; right: 0;
    top: 434px;
    text-align: center;
    color: var(--gold);
    font-weight: 600;
    font-size: 16px;
  }
  .ingredients-body {
    position: absolute;
    left: 38px; right: 38px;
    top: 458px;
    color: var(--ink-soft);
    font-size: 12.5px;
    line-height: 15px;
  }
</style>
</head>
<body>

  <section class="pouch pouch--front">
    <div class="pattern pattern--top" role="img" aria-label="Doodle pattern of peanut butter jars, waffles, coffee cups and peanuts"></div>
    <div class="pattern pattern--side-left" role="img" aria-label="Doodle pattern continued"></div>
    <div class="pattern pattern--side-right" role="img" aria-label="Doodle pattern continued"></div>

    <svg class="speech-bubble" viewBox="0 0 340 330" aria-hidden="true">
      <path d="M24 0 H316 Q340 0 340 24 V246 Q340 270 316 270 H150 Q128 272 140 318 Q104 300 100 270 H24 Q0 270 0 246 V24 Q0 0 24 0 Z" fill="var(--gold)"/>
    </svg>

    <h1 class="product-title">Peanut<br>Butter</h1>
    <p class="product-format">Single Serve Sachet</p>

    <p class="flavour-name">Tamarind Hill</p>
    <p class="variant">SMOOTH</p>
    <div class="knife" role="img" aria-label="Line drawing of a butter knife"></div>

    <div class="organic-band"></div>
    <p class="organic-label">ORGANIC</p>
    <p class="origin">CRAFTED IN INDIA 400G</p>
  </section>

  <section class="pouch pouch--back">
    <div class="pattern pattern--top" role="img" aria-label="Doodle pattern of peanut butter jars, waffles, coffee cups and peanuts"></div>
    <div class="pattern pattern--bottom" role="img" aria-label="Doodle pattern continued"></div>
    <div class="info-frame"></div>

    <p class="claim">Highest quality Peanuts<br>Roasted to perfection and<br>Blended until silky smooth.</p>
    <div class="knife" role="img" aria-label="Line drawing of a butter knife"></div>

    <p class="free-from">100% Chemical &amp; preservation Free</p>
    <p class="no-oils">NO ADDED OILS.</p>
    <p class="ingredients-line"><strong>INGREDIENTS:</strong> Organic Peanuts, Organic Peanuts, Organic Peanuts, Organic Peanuts</p>

    <p class="ingredients-heading">INGREDIENTS</p>
    <p class="ingredients-body">Lorem Ipsum is simply dummy text of the printing and typesetting industry. Lorem Ipsum has been the industry's standard dummy text ever since the 1500s, when an unknown printer took a galley of type and scrambled it to make a type specimen book. It has survived not only five centuries,</p>
  </section>

</body>
</html>
```